Letterhead and Business Card for our company

We need a letterhead to our company with Business Cards.. This will be printed. The letter head is the official use for the company.

Note: Put in consideration that 2 languages will be used, you will design the English and we will add the Arabic.

Company name: Brisk Harbor
City: Jeddah
District: Alrehab
Center: Palmgate Plaza
Country: Saudi Arabia
POBox: 3872 Jeddah 23619

Industry/Entity Type

Startup

Font styles to use
Sans Serif

Requirements
Must have
• Capital: 100,000
• CR: 4817293058

```html
<!DOCTYPE html>
<html lang="en">
<head>
<meta charset="utf-8">
<title>Brisk Harbor — Letterhead and Business Cards</title>
<link rel="stylesheet" href="https://fonts.googleapis.com/css2?family=Roboto:wght@400;500;700&display=swap">
<style>
  :root {
    --canvas: #ffffff;
    --paper: #f9f9f9;
    --card-dark: #35373c;
    --ink: #2f3035;
    --white: #ffffff;
    --plum: #9c1b5b;
    --red: #e0162b;
    --green: #78a316;
    --violet: #5c4e9d;
    --blue: #3d9bc8;
  }
  * { box-sizing: border-box; margin: 0; padding: 0; }
  html, body { width: 1200px; height: 1200px; overflow: hidden; background: var(--canvas); }
  body { position: relative; font-family: "Roboto", Arial, sans-serif; color: var(--ink); }

  .card {
    position: absolute; left: 160px; width: 256px; height: 155px;
    background: var(--card-dark); overflow: hidden;
  }
  .card--front { top: 435px; }
  .card--back { top: 609px; }

  .wordmark { position: absolute; display: flex; align-items: center; gap: 8px; white-space: nowrap; }
  .wordmark__dot { border-radius: 50%; background: var(--blue); flex: none; }
  .wordmark__name { font-weight: 500; letter-spacing: 0.5px; }

  .card--front .wordmark { left: 0; right: 0; top: 64px; justify-content: center; }
  .card--front .wordmark__dot { width: 16px; height: 16px; }
  .card--front .wordmark__name { font-size: 20px; color: var(--white); }

  .card--back .wordmark { left: 30px; top: 48px; }
  .card--back .wordmark__dot { width: 44px; height: 44px; }

  .stripe { position: absolute; left: 0; right: 0; bottom: 0; display: flex; }
  .stripe span { flex: 1; }
  .card--front .stripe { height: 5px; }
  .s-blue { background: var(--blue); }
  .s-green { background: var(--green); }
  .s-red { background: var(--red); }
  .s-plum { background: var(--plum); }
  .s-violet { background: var(--violet); }

  .contact { position: absolute; left: 132px; top: 31px; color: var(--white); }
  .contact__name { font-size: 10.5px; font-weight: 700; }
  .contact__role { font-size: 5px; opacity: 0.85; margin-top: 0; }
  .contact__list { list-style: none; margin-top: 10px; font-size: 6.2px; line-height: 9px; }
  .contact__list li { display: flex; align-items: center; gap: 6px; }
  .contact__list svg { width: 6px; height: 6px; fill: var(--white); flex: none; }
  .contact__address { font-size: 6.2px; line-height: 9.5px; margin-top: 2px; }

  .card--back .stripe { height: 12px; width: 110px; right: auto; }
  .band {
    position: absolute; background: var(--blue); color: var(--white);
    clip-path: polygon(8% 0, 100% 0, 100% 100%, 0 100%);
  }
  .card--back .band { left: 104px; right: 0; bottom: 0; height: 20px; font-size: 6.2px; padding: 6px 0 0 27px; }

  .letterhead {
    position: absolute; left: 448px; top: 182px; width: 591px; height: 836px;
    background: var(--paper); overflow: hidden;
  }
  .letterhead .wordmark { right: 58px; top: 60px; }
  .letterhead .wordmark__dot { width: 30px; height: 30px; }
  .letterhead .wordmark__name { font-size: 30px; color: var(--ink); }
  .letterhead__address { position: absolute; left: 32px; top: 782px; font-size: 10px; line-height: 13.5px; color: var(--ink); }
  .letterhead .stripe { height: 14px; width: 306px; }
  .letterhead .band { left: 300px; right: 0; bottom: 0; height: 34px; font-size: 10px; padding: 8px 0 0 72px; }
  .letterhead .band .sep { margin: 0 6px; }
</style>
</head>
<body>

  <section class="card card--front" aria-label="Business card front">
    <div class="wordmark">
      <span class="wordmark__dot"></span>
      <span class="wordmark__name">Brisk Harbor</span>
    </div>
    <div class="stripe"><span class="s-blue"></span><span class="s-green"></span><span class="s-red"></span><span class="s-plum"></span><span class="s-violet"></span></div>
  </section>

  <section class="card card--back" aria-label="Business card back">
    <div class="wordmark"><span class="wordmark__dot"></span></div>
    <div class="contact">
      <p class="contact__name">Brisk Harbor</p>
      <p class="contact__role">Managing Director</p>
      <ul class="contact__list">
        <li><svg viewBox="0 0 10 10"><rect x="2.5" y="0" width="5" height="10" rx="1"/></svg>+966 12 555 0148</li>
        <li><svg viewBox="0 0 10 10"><path d="M1 4h8v6H1zM3 1h4v2H3z"/></svg>+966 12 555 0192</li>
        <li><svg viewBox="0 0 10 10"><path d="M0 2h10v6H0zM0 2l5 3 5-3"/></svg>hello@briskharbor.sa</li>
      </ul>
      <p class="contact__address">3872 Jeddah 23619<br>Palmgate Plaza Jeddah Saudi Arabia</p>
    </div>
    <div class="stripe"><span class="s-plum"></span><span class="s-red"></span><span class="s-green"></span><span class="s-violet"></span></div>
    <div class="band">www.briskharbor.sa</div>
  </section>

  <section class="letterhead" aria-label="Letterhead">
    <div class="wordmark">
      <span class="wordmark__dot"></span>
      <span class="wordmark__name">Brisk Harbor</span>
    </div>
    <p class="letterhead__address">3872 Jeddah 23619<br>Palmgate Plaza Jeddah Saudi Arabia</p>
    <div class="stripe"><span class="s-plum"></span><span class="s-red"></span><span class="s-green"></span><span class="s-violet"></span></div>
    <div class="band">Capital: 100,000<span class="sep">|</span>CR: 4817293058</div>
  </section>

</body>
</html>
```